I need an 8 x 2.5 foot banner with our logo to the specific resolution and specs for PressKite. I have attached AI and EPS file of the logo. I also included a mock up, to scale, of how I'd like it to look: use the gray from the logo as the background and a reverse white logo. Finally, I have included the PressKite template PSD for this.

```html
<!DOCTYPE html>
<html lang="en">
<head>
<meta charset="utf-8">
<title>Harborline Media – PressKite Banner</title>
<link rel="stylesheet" href="https://fonts.googleapis.com/css2?family=Exo+2:wght@600&display=swap">
<style>
  :root {
    --page: #f1f1f1;
    --banner-gray: #6b6967;
    --reverse-white: #ffffff;
  }
  * { margin: 0; padding: 0; box-sizing: border-box; }
  html, body {
    width: 1200px;
    height: 2629px;
    overflow: hidden;
    background: var(--page);
  }
  .banner {
    position: absolute;
    left: 82px;
    top: 67px;
    width: 1037px;
    height: 2486px;
    background: var(--banner-gray);
    display: flex;
    flex-direction: column;
    justify-content: space-around;
    align-items: center;
  }
  .brand-name {
    font-family: "Exo 2", "Helvetica Neue", Arial, sans-serif;
    font-weight: 600;
    font-size: 150px;
    line-height: 1;
    letter-spacing: -1px;
    color: var(--reverse-white);
    white-space: nowrap;
  }
</style>
</head>
<body>
  <main class="banner">
    <p class="brand-name">harborline</p>
    <p class="brand-name">harborline</p>
    <p class="brand-name">harborline</p>
    <p class="brand-name">harborline</p>
  </main>
</body>
</html>
```